Chiropody and Podiatry Flyer

A6 Flyer for a Chiropody Clinic.
Need to use an existing company logo (upload available).
Flyer should promote three aspects of the practice;
1) General chiropody : Nail Cutting; Corn Removal; Ingrown Nails; Hard Skin Removal; Verruca Treatment; Diabetic Assessment; Nail Surgery.
2) Home Visits - chiropody in the comfort of your own home.
3) Biomechanical Assessments / Orthotics
Colours should comprise navy blue/green/white to complement existing logo.
Promotional Offer on flyer.

Industry/Entity Type

Clinic

```html
<!DOCTYPE html>
<html lang="en">
<head>
<meta charset="utf-8">
<title>Harbour Lane for Health – Chiropody Clinic Flyer</title>
<link rel="stylesheet" href="https://fonts.googleapis.com/css2?family=Open+Sans:wght@300;400;600&family=PT+Sans+Narrow:wght@700&display=swap">
<style>
  :root {
    --navy: #1b3f8f;
    --navy-deep: #0d2a63;
    --green: #4fb848;
    --black: #000000;
    --white: #ffffff;
    --ink: #1a1a1a;
    --backdrop: #145b88;
    --divider: #c9c9c9;
    --bullet: #2f6fc0;
  }
  * { box-sizing: border-box; margin: 0; padding: 0; }
  html, body { width: 1200px; height: 1200px; overflow: hidden; }
  body { background: var(--backdrop); position: relative; font-family: "Open Sans", sans-serif; }

  .flyer { position: absolute; background: var(--white); overflow: hidden; box-shadow: 0 6px 18px rgba(0,0,0,.35); }
  .flyer--front { left: 84px; top: 61px; width: 685px; height: 530px; }
  .flyer--back { left: 321px; top: 617px; width: 713px; height: 553px; }

  .shape-layer { position: absolute; inset: 0; }
  .abs { position: absolute; }

  .brand-box {
    position: absolute; background: linear-gradient(180deg, #1e3f8c, #0b1f4d);
    border: 2px solid var(--white); display: flex; align-items: center; justify-content: center;
    text-align: center; gap: 8px; padding: 8px;
  }
  .flyer--back .brand-box { border: none; }
  .brand-box__dot { width: 12px; height: 12px; border-radius: 50%; background: var(--green); flex: none; }
  .brand-box__name { color: var(--white); font-family: "Open Sans", sans-serif; font-weight: 600; font-size: 15px; line-height: 1.25; text-transform: uppercase; letter-spacing: .5px; }

  .headline { font-family: "PT Sans Narrow", sans-serif; font-weight: 700; line-height: 1; white-space: nowrap; }
  .clinic-title { left: 382px; top: 34px; font-size: 40px; color: var(--white); }
  .clinic-title span { color: var(--green); }
  .section-title { left: 410px; top: 117px; font-size: 27px; color: var(--white); }

  .service-list { left: 424px; top: 150px; list-style: none; color: var(--white); font-weight: 300; font-size: 17px; line-height: 27.2px; white-space: nowrap; }
  .service-list li { position: relative; padding-left: 15px; }
  .service-list li::before { content: ""; position: absolute; left: 0; top: 11px; width: 7px; height: 7px; border-radius: 50%; background: var(--bullet); }

  .xray-art { left: 0; top: 0; width: 410px; height: 364px;
    background: radial-gradient(ellipse at 62% 55%, rgba(200,30,30,.75), transparent 45%),
                radial-gradient(ellipse at 25% 60%, rgba(60,120,230,.6), transparent 50%), var(--black); }

  .booking { text-align: center; color: var(--white); font-family: "PT Sans Narrow", sans-serif; font-weight: 700; font-size: 26px; line-height: 24px; white-space: nowrap; }
  .contact { text-align: center; color: var(--navy); }
  .contact__email { font-size: 17px; }
  .contact__address { font-family: "PT Sans Narrow", sans-serif; font-weight: 700; font-size: 12px; margin-top: 6px; }

  .welcome { left: 262px; top: 380px; width: 356px; text-align: center; font-size: 12.4px; line-height: 16.5px; color: var(--ink); }

  .vline { position: absolute; width: 1px; background: var(--divider); }
  .badge-society { position: absolute; background: #e4e6ec; border-radius: 4px; }
  .badge-register { position: absolute; border: 2px solid var(--navy); background: linear-gradient(90deg, var(--navy) 0 35%, var(--white) 35%); }

  .intro { left: 232px; top: 41px; width: 468px; font-size: 16px; line-height: 21.3px; color: var(--ink); }
  .hline { position: absolute; height: 1px; background: #9a9a9a; }
  .home-title { left: 37px; top: 182px; font-size: 38px; line-height: 29px; color: var(--navy); }
  .home-note { left: 157px; top: 190px; font-size: 15px; font-weight: 600; line-height: 19.5px; color: var(--ink); }
  .sub-service { left: 36px; top: 258px; font-size: 20px; line-height: 19.5px; color: var(--ink); }
  .therapy-photo { left: 183px; top: 135px; width: 530px; height: 345px;
    background: radial-gradient(ellipse at 45% 45%, rgba(120,135,150,.55), transparent 55%),
                radial-gradient(ellipse at 85% 50%, rgba(120,190,215,.5), transparent 45%),
                linear-gradient(90deg, rgba(255,255,255,0), rgba(235,238,240,.9)); }
</style>
</head>
<body>

<section class="flyer flyer--front" aria-label="Flyer front: chiropody clinic">
  <div class="abs xray-art" role="img" aria-label="X-ray style image of two feet with the heel highlighted in red"></div>
  <svg class="shape-layer" width="685" height="530" viewBox="0 0 685 530" aria-hidden="true">
    <path d="M410 0 H685 V364 H410 Z" fill="var(--black)"/>
    <path d="M0 323 L244 364 L0 364 Z" fill="var(--white)"/>
    <polygon points="0,338 244,370 244,433 0,433" fill="var(--green)"/>
    <rect x="646" y="376" width="39" height="56" fill="var(--green)"/>
    <path d="M340 96 Q500 78 685 76 V96 Z" fill="var(--green)"/>
  </svg>

  <div class="brand-box" style="left:34px; top:30px; width:166px; height:114px;">
    <span class="brand-box__dot"></span>
    <span class="brand-box__name">Harbour Lane<br>for Health</span>
  </div>

  <h1 class="abs headline clinic-title">CHIROPODY <span>CLINIC</span></h1>
  <h2 class="abs headline section-title">GENERAL CHIROPODY</h2>
  <ul class="abs service-list">
    <li>Nail Cutting</li>
    <li>Corn Removal</li>
    <li>Ingrown Nails</li>
    <li>Hard Skin Removal</li>
    <li>Verruca Treatment</li>
    <li>Diabetic Assessment</li>
    <li>Nail Surgery.</li>
  </ul>

  <p class="abs booking" style="left:0; top:381px; width:250px;">BOOK APPOINTMENT<br>123 456 789</p>
  <div class="abs contact" style="left:0; top:441px; width:250px;">
    <p class="contact__email">youremail@clinic.com</p>
    <p class="contact__address">ADDRESS HERE</p>
  </div>

  <p class="abs welcome">Welcome to Chiropody Clinic and Footcare Centre offers comprehensive care of your feet, from removing hard skin to the nail surgery.</p>

  <span class="vline" style="left:271px; top:448px; height:56px;"></span>
  <div class="badge-society" style="left:290px; top:452px; width:150px; height:48px;" role="img" aria-label="Professional society membership badge"></div>
  <span class="vline" style="left:460px; top:448px; height:56px;"></span>
  <div class="badge-register" style="left:476px; top:458px; width:150px; height:29px;" role="img" aria-label="Professional registration badge"></div>
</section>

<section class="flyer flyer--back" aria-label="Flyer back: home visits and biomechanics">
  <div class="abs therapy-photo" role="img" aria-label="Photo of a podiatrist assessing a seated patient's foot and leg stretch"></div>
  <svg class="shape-layer" width="713" height="553" viewBox="0 0 713 553" aria-hidden="true">
    <polygon points="0,353 254,391 254,451 0,451" fill="var(--green)"/>
    <rect x="674" y="391" width="39" height="59" fill="var(--green)"/>
  </svg>

  <div class="brand-box" style="left:36px; top:33px; width:170px; height:116px;">
    <span class="brand-box__dot"></span>
    <span class="brand-box__name">Harbour Lane<br>for Health</span>
  </div>

  <p class="abs intro">The Guild of Foot Care exists to ensure the public has access to high quality foot care delivered by qualified and regulated professionals. The Association of Foot Practitioners is the leading professional body and trade union for chiropodists and podiatrists.</p>

  <span class="hline" style="left:36px; top:171px; width:328px;"></span>
  <h2 class="abs headline home-title">HOME<br>VISITS</h2>
  <p class="abs home-note">Chiropody in the comfort of<br>your own home.</p>
  <span class="hline" style="left:36px; top:248px; width:328px;"></span>
  <p class="abs headline sub-service">BIOMECHANICAL ASSESSMENTS /<br>ORTHOTICS</p>

  <p class="abs booking" style="left:0; top:397px; width:262px; font-size:27px; line-height:28px;">BOOK APPOINTMENT<br>123 456 789</p>
  <div class="abs contact" style="left:0; top:461px; width:252px;">
    <p class="contact__email">youremail@clinic.com</p>
    <p class="contact__address">ADDRESS HERE</p>
  </div>

  <span class="vline" style="left:282px; top:466px; height:58px;"></span>
  <div class="badge-society" style="left:303px; top:469px; width:156px; height:52px;" role="img" aria-label="Professional society membership badge"></div>
  <span class="vline" style="left:479px; top:466px; height:58px;"></span>
  <div class="badge-register" style="left:496px; top:477px; width:156px; height:30px;" role="img" aria-label="Professional registration badge"></div>
</section>

</body>
</html>
```